Owen Tasker Studios Business Card

Looking for a clear, modern, elegant, sharp business card that conveys a professional yet edgy image to my business as a wedding, portrait, and travel photographer. Would like something that looks vintage yet modern. Need a new business card to grow my business. We are growing the business for Wedding and Event Photography as well as fine art Photography. (Mostly Landscapes)
Updates

I’m looking through designs now but I have a new logo that i want using please.

New logo uploaded please redesign using that

PLEASE ALL DESIGNERS LOOK IN BRIEF FOR NEW LOGO

Target Market(s)

Brides, Grooms, Families with Kids, People looking for Fine Art Photography Artwork

Industry/Entity Type

Photographer

Contact Information for Business Card

Unsure

Font styles to use
Serif

Colors

Designer to choose colors to be used in the design.

Requirements
Must have
• My Website:
• http://taskerlens.examplefolio.net
• Phone:
• 323-481-5206
• Email:
• owentaskerlens@mailbox-example.net
Nice to have
• Would like a sort of shine on the printing finish.
• I like black I think it looks good on a business card.
• Can try working with my logo (png that I've attached)

```html
<!DOCTYPE html>
<html lang="en">
<head>
<meta charset="utf-8">
<title>Owen Tasker Studios – Business Card</title>
<link rel="stylesheet" href="https://fonts.googleapis.com/css2?family=Didact+Gothic&family=Lato:wght@400;900&display=swap">
<style>
  :root {
    --sheet: #e6e6e6;
    --card: #000000;
    --ink-dark: #111111;
    --ink-light: #ffffff;
    --accent: #ff6a00;
    --shadow: rgba(0, 0, 0, 0.35);
  }
  * { margin: 0; padding: 0; box-sizing: border-box; }
  html, body { width: 1200px; height: 2510px; overflow: hidden; }
  body {
    background: var(--sheet);
    position: relative;
    font-family: "Lato", Arial, sans-serif;
  }

  .brand-mark {
    position: absolute;
    left: 50%;
    transform: translateX(-50%);
    border: 4px solid currentColor;
  }
  .brand-name,
  .brand-studios {
    position: absolute;
    left: 0;
    width: 100%;
    text-align: center;
    font-family: "Didact Gothic", "Century Gothic", sans-serif;
    font-weight: 400;
    white-space: nowrap;
    line-height: 1;
  }

  /* Master lockup on the sheet */
  .lockup { position: absolute; left: 0; top: 0; width: 1200px; height: 540px; color: var(--ink-dark); }
  .lockup .brand-mark { top: 114px; width: 190px; height: 190px; border-width: 5px; }
  .lockup .brand-name { top: 368px; font-size: 88px; letter-spacing: 1px; }
  .lockup .brand-studios { top: 470px; font-size: 40px; letter-spacing: 30px; padding-left: 30px; }

  /* Cards */
  .card {
    position: absolute;
    background: var(--card);
    border-radius: 28px;
    box-shadow: 0 10px 22px var(--shadow);
    color: var(--ink-light);
    overflow: hidden;
  }
  .card--portrait { width: 458px; height: 759px; top: 602px; }
  .card--landscape { width: 763px; height: 458px; left: 229px; }
  .card--front-portrait { left: 125px; }
  .card--back-portrait { left: 638px; }
  .card--front-landscape { top: 1446px; }
  .card--back-landscape { top: 1952px; }

  .card .brand-mark { width: 112px; height: 112px; border-width: 3px; }
  .card .brand-name { font-size: 48px; }
  .card .brand-studios { font-size: 23px; letter-spacing: 15px; padding-left: 15px; }

  .card--front-portrait .brand-mark { top: 151px; }
  .card--front-portrait .brand-name { top: 305px; }
  .card--front-portrait .brand-studios { top: 366px; }

  .card--front-landscape .brand-mark { top: 68px; }
  .card--front-landscape .brand-name { top: 218px; }
  .card--front-landscape .brand-studios { top: 279px; }

  .website {
    position: absolute;
    left: 0;
    width: 100%;
    text-align: center;
    color: var(--accent);
    font-size: 25px;
    line-height: 1;
  }
  .card--front-portrait .website { top: 697px; font-size: 23px; }
  .card--front-landscape .website { top: 380px; font-size: 27px; }

  /* Back, portrait */
  .card--back-portrait .square-mark {
    position: absolute;
    right: 56px;
    top: 78px;
    width: 160px;
    height: 160px;
    border: 4px solid var(--ink-light);
  }
  .person-name {
    font-weight: 900;
    line-height: 1;
    letter-spacing: 2px;
  }
  .person-name .surname { color: var(--accent); }
  .card--back-portrait .person-name {
    position: absolute;
    left: 40px;
    top: 330px;
    font-size: 72px;
  }
  .card--back-portrait .person-name span { display: block; margin-bottom: 4px; }
  .card--back-portrait .contact {
    position: absolute;
    right: 30px;
    top: 532px;
    text-align: right;
    font-size: 22px;
    line-height: 36px;
  }
  .email { color: var(--accent); }
  .phone { color: var(--ink-light); }

  /* Back, landscape */
  .card--back-landscape .person-name {
    position: absolute;
    left: 0;
    width: 100%;
    top: 170px;
    text-align: center;
    font-size: 72px;
  }
  .card--back-landscape .contact {
    position: absolute;
    left: 0;
    width: 100%;
    top: 245px;
    text-align: center;
    font-size: 24px;
    line-height: 1;
  }
  .divider {
    display: inline-block;
    width: 2px;
    height: 28px;
    background: var(--ink-light);
    margin: 0 10px;
    vertical-align: -6px;
  }
</style>
</head>
<body>

  <section class="lockup" aria-label="Owen Tasker Studios brand lockup">
    <div class="brand-mark"></div>
    <div class="brand-name">OWEN TASKER</div>
    <div class="brand-studios">STUDIOS</div>
  </section>

  <article class="card card--portrait card--front-portrait">
    <div class="brand-mark"></div>
    <div class="brand-name">OWEN TASKER</div>
    <div class="brand-studios">STUDIOS</div>
    <div class="website">taskerlens.examplefolio.net</div>
  </article>

  <article class="card card--portrait card--back-portrait">
    <div class="square-mark"></div>
    <h2 class="person-name"><span>OWEN</span><span class="surname">TASKER</span></h2>
    <div class="contact">
      <div class="email">owentaskerlens@mailbox-example.net</div>
      <div class="phone">323-481-5206</div>
    </div>
  </article>

  <article class="card card--landscape card--front-landscape">
    <div class="brand-mark"></div>
    <div class="brand-name">OWEN TASKER</div>
    <div class="brand-studios">STUDIOS</div>
    <div class="website">taskerlens.examplefolio.net</div>
  </article>

  <article class="card card--landscape card--back-landscape">
    <h2 class="person-name">OWEN <span class="surname">TASKER</span></h2>
    <div class="contact">
      <span class="email">owentaskerlens@mailbox-example.net</span><span class="divider"></span><span class="phone">323-481-5206</span>
    </div>
  </article>

</body>
</html>
```